Linked In Profile Banner Needed

I am in need of a Linked In Banner photo for my profile. The dimensions are 1584 x 396 pixels and the bottom left is where Linked In places my photo over so be aware of that. I attached an example for your reference.

I have also attached my logo and business card so you can keep the same color & style conistant.

Also add the following text:

"Preserve capital with a tax advantaged lease for equipment, vehicles, software and more! $5,000 - $50m"

You can also look at our website here:
www.HarlowfieldFundingCo.com

```html
<!DOCTYPE html>
<html lang="en">
<head>
<meta charset="utf-8">
<title>Harlowfield Funding Co. – Profile Banner</title>
<link href="https://fonts.googleapis.com/css2?family=Rubik:wght@400;500;600;700&display=swap" rel="stylesheet">
<style>
  :root {
    --navy-light: #34345f;
    --navy-mid: #242446;
    --navy-dark: #141428;
    --cyan: #00d1ff;
    --ring: #3a8fd0;
    --violet: #5b5aa3;
    --white: #ffffff;
    --ink: #0b0b14;
  }
  * { margin: 0; padding: 0; box-sizing: border-box; }
  html, body { width: 1200px; height: 301px; overflow: hidden; background: var(--white); }
  .banner {
    position: relative;
    width: 1200px;
    height: 301px;
    overflow: hidden;
    font-family: "Rubik", sans-serif;
    background: linear-gradient(90deg, var(--navy-light) 0%, var(--navy-mid) 45%, var(--navy-dark) 100%);
  }
  .banknote-photo {
    position: absolute;
    left: 330px;
    top: 0;
    width: 520px;
    height: 243px;
    background: radial-gradient(ellipse at 50% 40%, rgba(140,140,170,0.22) 0%, rgba(90,90,130,0.12) 45%, rgba(0,0,0,0) 75%);
  }
  .shapes { position: absolute; inset: 0; }
  .brand {
    position: absolute;
    left: 902px;
    top: 36px;
    display: flex;
    align-items: center;
    gap: 10px;
    color: var(--white);
  }
  .brand-mark {
    width: 30px;
    height: 36px;
    background: var(--ring);
  }
  .brand-name {
    font-size: 19px;
    font-weight: 400;
    letter-spacing: 0.5px;
    line-height: 1.1;
  }
  .headline {
    position: absolute;
    left: 351px;
    top: 96px;
    color: var(--white);
  }
  .headline-lead { font-size: 21px; font-weight: 400; line-height: 26px; }
  .headline-main {
    font-size: 42px;
    font-weight: 600;
    color: var(--cyan);
    line-height: 48px;
    margin-top: 0;
  }
  .headline-tail { font-size: 21px; font-weight: 400; line-height: 28px; margin-top: 2px; }
  .price-tag {
    position: absolute;
    left: 872px;
    top: 120px;
    width: 263px;
    height: 52px;
    border-radius: 9px;
    background: var(--cyan);
    color: var(--ink);
    font-size: 27px;
    font-weight: 700;
    display: flex;
    align-items: center;
    justify-content: center;
    box-shadow: 0 4px 10px rgba(0,0,0,0.35);
  }
</style>
</head>
<body>
<div class="banner">
  <div class="banknote-photo" role="img" aria-label="Faint background photo of stacked banknotes"></div>

  <svg class="shapes" width="1200" height="301" viewBox="0 0 1200 301">
    <defs>
      <radialGradient id="disc-fill" cx="0.5" cy="0.5" r="0.5">
        <stop offset="0.8" stop-color="#6a63b0"/>
        <stop offset="1" stop-color="#4a4a8c"/>
      </radialGradient>
    </defs>
    <g class="outer-rings" fill="none" stroke="var(--ring)">
      <circle cx="163" cy="254" r="190" stroke-width="2" opacity="0.12"/>
      <circle cx="163" cy="254" r="178" stroke-width="3" opacity="0.2"/>
      <circle cx="163" cy="254" r="166" stroke-width="3" opacity="0.3"/>
      <circle cx="163" cy="254" r="154" stroke-width="4" opacity="0.45"/>
    </g>
    <circle cx="163" cy="254" r="138" fill="url(#disc-fill)"/>
    <circle cx="163" cy="254" r="136" fill="none" stroke="var(--cyan)" stroke-width="4"/>
    <rect class="base-band" x="0" y="243" width="1200" height="58" fill="var(--cyan)"/>
    <circle class="profile-slot" cx="163" cy="254" r="119" fill="var(--white)"/>
  </svg>

  <div class="brand">
    <div class="brand-mark"></div>
    <div class="brand-name">HARLOWFIELD FUNDING CO.</div>
  </div>

  <div class="headline">
    <p class="headline-lead">Preserve capital with a</p>
    <p class="headline-main">Tax Advantaged Lease</p>
    <p class="headline-tail">for equipment, vehicles, software and more!</p>
  </div>

  <div class="price-tag">$5,000 - $50m</div>
</div>
</body>
</html>
```